Stationary and business card design for dental office
Dental Harbor
Simple
Merrow T. Pashley, DMD
Dental Harbor (use logo)
2870 W. Cobalt Mesa Rd. Ste #6
Las Vegas, NV 89047
pashleydmd@quarvix-mail.test
www.ourdentalharbor.test
Front of card to be gloss finish with the back to be a regular paper finish so that appointments can be written on the back.
My Next Appointment
Date:___________
Time:____________
Days of the week with boxes
Call Now
A simple map of the location to the right

```html
<!DOCTYPE html>
<html lang="en">
<head>
<meta charset="utf-8">
<title>Dental Harbor Stationery</title>
<link href="https://fonts.googleapis.com/css2?family=Open+Sans:wght@400;600;700&display=swap" rel="stylesheet">
<style>
:root{
  --ink:#3a3a3c;
  --band:#3d3d40;
  --teal:#22a3a3;
  --green:#8cc63f;
  --muted:#8a8a8d;
  --paper:#ffffff;
  --edge:#d9d9d9;
  --ghost:#e9f3ef;
  --map:#e6ece6;
}
*{box-sizing:border-box;margin:0;padding:0}
html,body{width:1200px;height:480px;overflow:hidden;background:#fff}
body{position:relative;font-family:"Open Sans",Arial,sans-serif;color:var(--ink)}
.sheet{position:absolute;background:var(--paper);border:1px solid var(--edge);box-shadow:0 1px 3px rgba(0,0,0,.12);overflow:hidden}
.header-band{position:absolute;top:0;right:0;width:70%;height:34px}
.brand{position:absolute;display:flex;align-items:center;gap:6px}
.brand-dot{width:14px;height:14px;border-radius:50%;background:var(--teal);flex:none}
.brand-name{font-weight:700;font-size:13px;letter-spacing:.06em;text-transform:uppercase;color:var(--ink);line-height:1}
.ghost-mark{position:absolute;left:50%;transform:translateX(-50%);display:flex;flex-direction:column;align-items:center;gap:8px}
.ghost-mark .ring{width:110px;height:110px;border-radius:50%;background:var(--ghost)}
.ghost-mark .ghost-name{font-weight:700;font-size:13px;letter-spacing:.08em;text-transform:uppercase;color:#e2ece8}
.footer-text{position:absolute;bottom:16px;left:0;right:0;text-align:center;font-size:5.5px;line-height:1.6;color:var(--muted)}

/* fax sheet */
.fax{left:19px;top:19px;width:305px;height:442px}
.fax .brand{left:22px;top:30px}
.fax-fields{position:absolute;left:22px;top:138px;width:260px;display:grid;grid-template-columns:1fr 1fr;row-gap:9px;column-gap:20px;font-size:7px;font-weight:600}
.field{display:flex;gap:6px}
.field .line{flex:1;border-bottom:1px solid #bbb;height:8px}
.fax-checks{position:absolute;left:22px;top:220px;display:flex;gap:9px;font-size:6px;font-weight:600}
.check{display:flex;align-items:center;gap:3px}
.check i{width:6px;height:6px;border:1px solid var(--ink)}
.fax .ghost-mark{top:262px}

/* envelopes */
.envelope{left:360px;width:336px;height:162px}
.envelope-front{top:101px}
.envelope-front .brand{left:14px;top:14px}
.return-address{position:absolute;left:14px;top:40px;font-size:5.5px;line-height:1.5;color:var(--muted)}
.envelope-back{top:283px}
.envelope-back svg.flap{position:absolute;inset:0;width:100%;height:100%}
.envelope-back .seal{position:absolute;left:50%;top:70px;transform:translateX(-50%);width:16px;height:16px;border-radius:50%;background:var(--teal)}

/* letterhead */
.letterhead{left:768px;top:19px;width:276px;height:442px}
.letterhead .brand{left:20px;top:30px}
.letterhead .ghost-mark{top:230px;left:62%}

/* business cards */
.card{left:1032px;width:150px;height:80px;border-radius:2px}
.card-front{top:84px}
.card-front .header-band{height:16px}
.card-front .brand{left:8px;top:8px;gap:4px}
.card-front .brand-dot{width:9px;height:9px}
.card-front .brand-name{font-size:8px}
.card-info{position:absolute;left:8px;top:26px;font-size:4.6px;line-height:1.45;color:var(--muted)}
.card-info .name{font-size:6px;font-weight:700;color:var(--ink)}
.card-back{top:173px}
.appt{position:absolute;left:7px;top:7px;width:80px;font-size:4.8px;line-height:1.6}
.appt h3{font-size:6px;font-weight:700;color:var(--teal)}
.appt .slot{display:flex;gap:3px}
.appt .slot span.line{flex:1;border-bottom:.6px solid #aaa;height:6px}
.days{display:flex;gap:3px;margin-top:2px}
.days span{display:flex;flex-direction:column;align-items:center;font-size:4px}
.days i{width:6px;height:6px;border:.6px solid var(--ink);margin-top:1px}
.call-now{margin-top:3px;font-weight:700;font-size:5px;color:var(--ink)}
.map-area{position:absolute;right:7px;top:10px;width:52px;height:58px;background:linear-gradient(135deg,var(--map),#d3dcd6);border:.6px solid #c5cdc7}
</style>
</head>
<body>

<svg width="0" height="0" style="position:absolute">
  <defs>
    <symbol id="band" viewBox="0 0 200 34" preserveAspectRatio="none">
      <path d="M0 0 H200 V30 C150 22 90 20 40 14 C25 12 10 6 0 0Z" fill="#3d3d40"/>
      <path d="M0 0 C10 6 25 12 40 14 C90 20 150 22 200 30 V33 C150 25 90 23 38 17 C22 15 8 8 0 0Z" fill="#22a3a3"/>
      <path d="M0 0 C8 8 22 15 38 17 C90 23 150 25 200 33 V34 C150 27 88 25 36 19 C20 17 6 9 0 0Z" fill="#8cc63f"/>
    </symbol>
  </defs>
</svg>

<section class="sheet fax">
  <svg class="header-band"><use href="#band"/></svg>
  <div class="brand"><span class="brand-dot"></span><span class="brand-name">Dental Harbor</span></div>
  <div class="fax-fields">
    <div class="field">To:<span class="line"></span></div>
    <div class="field">From:<span class="line"></span></div>
    <div class="field">Fax:<span class="line"></span></div>
    <div class="field">Pages:<span class="line"></span></div>
    <div class="field">Phone:<span class="line"></span></div>
    <div class="field">Date:<span class="line"></span></div>
    <div class="field">Re:<span class="line"></span></div>
    <div class="field">CC:<span class="line"></span></div>
  </div>
  <div class="fax-checks">
    <span class="check"><i></i>Urgent</span>
    <span class="check"><i></i>For Review</span>
    <span class="check"><i></i>Please Comment</span>
    <span class="check"><i></i>Please Reply</span>
    <span class="check"><i></i>Please Recycle</span>
  </div>
  <div class="ghost-mark"><span class="ring"></span><span class="ghost-name">Dental Harbor</span></div>
  <p class="footer-text">2870 W. Cobalt Mesa Rd. Ste #6 · Las Vegas, NV 89047<br>Phone 702.555.0148 · Fax 702.555.0149 · pashleydmd@quarvix-mail.test</p>
</section>

<section class="sheet envelope envelope-front">
  <svg class="header-band" style="width:0"></svg>
  <div class="brand"><span class="brand-dot"></span><span class="brand-name">Dental Harbor</span></div>
  <p class="return-address">2870 W. Cobalt Mesa Rd. Ste #6<br>Las Vegas, NV 89047</p>
</section>

<section class="sheet envelope envelope-back">
  <svg class="flap" viewBox="0 0 336 162" preserveAspectRatio="none">
    <path d="M0 0 L168 64 L336 0" fill="none" stroke="#bdbdbd" stroke-width="1"/>
    <path d="M0 162 L130 84 M336 162 L206 84" fill="none" stroke="#e0e0e0" stroke-width="1"/>
  </svg>
  <span class="seal"></span>
</section>

<section class="sheet letterhead">
  <svg class="header-band"><use href="#band"/></svg>
  <div class="brand"><span class="brand-dot"></span><span class="brand-name">Dental Harbor</span></div>
  <p class="footer-text" style="text-align:left;left:20px;top:76px;bottom:auto">2870 W. Cobalt Mesa Rd. Ste #6<br>Las Vegas, NV 89047</p>
  <div class="ghost-mark"><span class="ring"></span><span class="ghost-name">Dental Harbor</span></div>
</section>

<section class="sheet card card-front">
  <svg class="header-band"><use href="#band"/></svg>
  <div class="brand"><span class="brand-dot"></span><span class="brand-name">Dental Harbor</span></div>
  <div class="card-info">
    <p class="name">Merrow T. Pashley, DMD</p>
    <p>2870 W. Cobalt Mesa Rd. Ste #6</p>
    <p>Las Vegas, NV 89047</p>
    <p>Phone 702.555.0148</p>
    <p>pashleydmd@quarvix-mail.test</p>
    <p>www.ourdentalharbor.test</p>
  </div>
</section>

<section class="sheet card card-back">
  <div class="appt">
    <h3>My Next Appointment</h3>
    <div class="slot">Date:<span class="line"></span></div>
    <div class="slot">Time:<span class="line"></span></div>
    <div class="days">
      <span>M<i></i></span><span>T<i></i></span><span>W<i></i></span><span>T<i></i></span><span>F<i></i></span><span>S<i></i></span>
    </div>
    <p class="call-now">Call Now 702.555.0148</p>
  </div>
  <div class="map-area" role="img" aria-label="Simple street map showing the office location"></div>
</section>

</body>
</html>
```